Fiscal Sponsorship Program Flyer

We are seeking a designer to create a 1-2 flyer that explains our fiscal sponsorship program. This flyer will be used to recruit new projects that might be interested in utilizing our fiscal sponsorship services. The pertinent information about our program can be found in the attached PDF. For users who cannot access the PDF, please try this link: https://files.plovarimedia.net/deck/7QtR2wzoLkVa9pXcJ4nEuYhsT3bGdMf8eKqW5rZxN1yo/view?mode=public

Target Market(s)

New charitable projects that do not yet have their own 501(c)(3) status, and are seeking a fiscal sponsor.

Industry/Entity Type

Nonprofit/Charity

Requirements
Must have
• The flyer must include the language and detail included on the attached PDF. The desire is to reformat this to be more appealing and easy to read.

```html
<!DOCTYPE html>
<html lang="en">
<head>
<meta charset="utf-8">
<title>Keystone Commons Foundation – Fiscal Sponsorship Program</title>
<link rel="stylesheet" href="https://fonts.googleapis.com/css2?family=Playfair+Display:wght@400;700;900&family=Montserrat:wght@400;500;600;700&display=swap">
<style>
  :root {
    --backdrop: #00118a;
    --paper: #ffffff;
    --slate: #616b6b;
    --red: #ec1c24;
    --ink: #3a3a3a;
    --black: #111111;
    --rule: #b9bdbd;
  }
  * { box-sizing: border-box; margin: 0; padding: 0; }
  html, body { width: 1200px; height: 857px; overflow: hidden; }
  body { background: var(--backdrop); position: relative; font-family: "Playfair Display", Georgia, serif; color: var(--ink); }

  .page { position: absolute; top: 109px; width: 451px; height: 639px; background: var(--paper); overflow: hidden; }
  .page--front { left: 125px; }
  .page--back { left: 619px; }

  .deco { position: absolute; left: 0; top: 0; }

  .masthead { position: absolute; left: 0; top: 0; width: 451px; text-align: center; color: #fff; }
  .masthead__name { position: absolute; left: 0; width: 440px; top: 26px; font-weight: 700; font-size: 45px; line-height: 1; letter-spacing: -0.3px; }
  .masthead__program { position: absolute; left: 0; width: 440px; top: 86px; font-weight: 400; font-size: 29px; line-height: 1; }

  .section-title { position: absolute; color: var(--red); font-weight: 900; font-size: 18px; line-height: 1; text-transform: uppercase; letter-spacing: -0.2px; }
  .copy { position: absolute; font-size: 10.2px; line-height: 14px; letter-spacing: -0.1px; }
  .copy--loose { line-height: 15.8px; }

  .values, .commitments { position: absolute; list-style: none; }
  .values li, .commitments li { position: relative; font-size: 10.2px; line-height: 15.5px; letter-spacing: -0.1px; }
  .values li::before, .commitments li::before { content: ""; position: absolute; left: -10px; top: 5px; width: 5px; height: 5px; border-radius: 50%; background: var(--black); }
  .values li { margin-bottom: 7.5px; }
  .values strong { color: var(--red); font-weight: 700; font-size: 11.5px; }
  .commitments li { line-height: 13px; margin-bottom: 6.5px; }

  .footer { position: absolute; left: 0; top: 603px; width: 451px; height: 36px; }
  .contact { position: absolute; top: 603px; height: 36px; display: flex; align-items: center; font-family: "Montserrat", Arial, sans-serif; color: #fff; }
  .contact__label { font-weight: 600; font-size: 11.2px; letter-spacing: 0.4px; margin-right: 10px; }
  .contact__item { display: flex; align-items: center; font-size: 7.6px; letter-spacing: 0.6px; margin-right: 9px; }
  .contact__item svg { margin-right: 5px; }

  .fee-heading { position: absolute; left: 102px; top: 356px; width: 255px; height: 45px; display: flex; align-items: center; justify-content: center; font-weight: 900; font-size: 27px; color: var(--black); letter-spacing: 0.3px; }

  .tier { position: absolute; top: 421px; width: 128px; height: 151px; border: 1px solid var(--rule); border-top: none; font-family: "Montserrat", Arial, sans-serif; }
  .tier__band { height: 28px; margin: 0 -1px; background: var(--red); border-radius: 7px 7px 0 0; color: #fff; font-weight: 700; font-size: 7.4px; letter-spacing: 0.9px; display: flex; align-items: center; justify-content: center; }
  .tier__name { margin: 6px 0 0 8px; font-weight: 600; font-size: 9.2px; letter-spacing: 0.8px; color: var(--black); }
  .tier__list { list-style: none; margin: 3px 0 0 8px; }
  .tier__list li { font-size: 5.3px; line-height: 11.4px; font-weight: 500; letter-spacing: 0.45px; color: var(--black); white-space: nowrap; }
  .tier--basic { left: 24px; }
  .tier--standard { left: 165px; }
  .tier--premium { left: 304px; }
</style>
</head>
<body>

<!-- Front page -->
<section class="page page--front">
  <svg class="deco" width="451" height="639" viewBox="0 0 451 639" aria-hidden="true">
    <path d="M0 0H451V100C432 128 404 146 372 146H0Z" fill="var(--slate)"/>
    <path d="M0 162H380C410 162 432 145 451 112" fill="none" stroke="var(--slate)" stroke-width="3" stroke-dasharray="3 14.3"/>
    <path d="M4 639C20 612 50 592 90 592H451" fill="none" stroke="var(--slate)" stroke-width="3" stroke-dasharray="3 14.3"/>
    <path d="M12 639C30 616 45 603 70 603H451V639Z" fill="var(--slate)"/>
  </svg>

  <header class="masthead">
    <h1 class="masthead__name">Keystone Commons</h1>
    <p class="masthead__program">Fiscal Sponsorship Program</p>
  </header>

  <h2 class="section-title" style="left:27px;top:181px;">Mission &amp; Vision</h2>
  <p class="copy" style="left:27px;top:209px;width:400px;">The Keystone Commons Foundation, founded in 2010, exists to support social impact campaigns and organizations through educational, public engagement, and awareness efforts.</p>
  <p class="copy" style="left:27px;top:252px;width:400px;">Its vision is to strengthen the capacity of the social impact sector and its leaders by providing top-tier fiscal sponsorship services.</p>

  <h2 class="section-title" style="left:26px;top:294px;">Organizational Values</h2>
  <ul class="values" style="left:26px;top:321px;width:400px;">
    <li><strong>Trust:</strong> We believe that all successful partnerships begin with a foundation of trust.</li>
    <li><strong>Relationships:</strong> Our partners are central to our work. We honor our relationships through respect, communication and transparency.</li>
    <li><strong>Embrace Complexity and Risk:</strong> We understand that bold solutions to intractable social issues often require both complexity and risk.</li>
    <li><strong>Innovation:</strong> We embrace continuous improvement, bold creativity and change.</li>
    <li><strong>Diversity:</strong> We believe that all voices matter and that effective solutions are created when decision-making is inclusive across social, cultural and economic backgrounds.</li>
  </ul>

  <h2 class="section-title" style="left:27px;top:486px;">What is Fiscal Sponsorship?</h2>
  <p class="copy copy--loose" style="left:27px;top:511px;width:405px;">Fiscal sponsorship refers to the practice of non-profit organizations offering their legal and tax-exempt status to charitable projects or groups engaged in activities related to the sponsoring organization's mission. Fiscal sponsors provide oversight, financial management, and other administrative services to build the capacity of charitable projects.</p>

  <div class="contact" style="left:70px;">
    <span class="contact__label">CONTACT US!</span>
    <span class="contact__item"><svg width="12" height="9" viewBox="0 0 12 9" aria-hidden="true"><rect width="12" height="9" fill="var(--red)"/><path d="M0 0L6 5L12 0" fill="none" stroke="#fff" stroke-width="1"/></svg>info@keystonecommons.org</span>
    <span class="contact__item"><svg width="11" height="11" viewBox="0 0 11 11" aria-hidden="true"><circle cx="5.5" cy="5.5" r="4.7" fill="none" stroke="var(--red)" stroke-width="1.4"/><circle cx="5.5" cy="5.5" r="2" fill="var(--red)"/></svg>keystonecommons.org</span>
  </div>
</section>

<!-- Back page -->
<section class="page page--back">
  <svg class="deco" width="451" height="639" viewBox="0 0 451 639" aria-hidden="true">
    <path d="M4 639C20 612 50 592 90 592H451" fill="none" stroke="var(--slate)" stroke-width="3" stroke-dasharray="3 14.3"/>
    <path d="M12 639C30 616 45 603 70 603H451V639Z" fill="var(--slate)"/>
    <line x1="29" y1="379" x2="102" y2="379" stroke="var(--rule)" stroke-width="1"/>
    <line x1="357" y1="379" x2="428" y2="379" stroke="var(--rule)" stroke-width="1"/>
    <path d="M124 356H335L357 379L335 401H124L102 379Z" fill="#fff" stroke="var(--rule)" stroke-width="1"/>
  </svg>

  <h2 class="section-title" style="left:39px;top:36px;">Program Philosophy</h2>
  <p class="copy" style="left:38px;top:65px;width:405px;">We believe we can accelerate the pace and scale of social change by providing strategic back office support to emerging projects, leaders and ideas.</p>
  <p class="copy" style="left:38px;top:106px;width:405px;">By providing light touch administrative and capacity building services, our fiscal sponsorship program takes the administrative burden off the shoulders of leaders and their projects to allow them to focus on what they do best - achieving impact and changing the world.</p>

  <h2 class="section-title" style="left:39px;top:164px;">Program Commitments</h2>
  <ul class="commitments" style="left:39px;top:192px;width:395px;">
    <li>Fast, simple and efficient fiscal sponsorship program</li>
    <li>Free and fast approval process - our application can be completed in 30 minutes or less. There is no fee to apply, and most projects can expect to receive a response on their application within 2 weeks</li>
    <li>No fees and no minimums; projects of any size are welcome to apply</li>
    <li>Easy onboarding process</li>
    <li>Dedicated customer service and customization of services, tailored to the individual sponsored project's needs</li>
    <li>Complex, hybrid structures, partnerships and coalitions are strongly encouraged to apply</li>
  </ul>

  <h2 class="fee-heading">FEE STRUCTURE</h2>

  <article class="tier tier--basic">
    <div class="tier__band">BASIC | FEE - 4%</div>
    <h3 class="tier__name">Limited</h3>
    <ul class="tier__list">
      <li>- Project Fund Set-Up</li>
      <li>- Administration and Management</li>
      <li>- Financial Management</li>
      <li>- Grant Proposal Review</li>
      <li>- Grant Contract Review</li>
      <li>- Project Reporting</li>
      <li>- Insurance</li>
      <li>- Annual Audit and Form 990</li>
    </ul>
  </article>

  <article class="tier tier--standard">
    <div class="tier__band">STANDARD | FEE - 6%</div>
    <h3 class="tier__name">Comprehensive</h3>
    <ul class="tier__list">
      <li>Basic Services +</li>
      <li>- Customized Financial Reporting</li>
      <li>- Monthly Financial Statements</li>
      <li>- Subgranting/regranting to U.S.</li>
      <li>based organizations</li>
      <li>-Management of Vendor and</li>
      <li>Independent Contractors (1099s)</li>
    </ul>
  </article>

  <article class="tier tier--premium">
    <div class="tier__band">PREMIUM | FEE - 10% +</div>
    <h3 class="tier__name">Custom</h3>
    <ul class="tier__list">
      <li>Standard Services + custom services</li>
      <li>tailored to individual project needs.</li>
      <li>Customization Options:</li>
      <li>- Subgranting/regranting to</li>
      <li>international organizations</li>
      <li>- Lobbying Filings</li>
      <li>- Project Audit</li>
      <li>- Grant Writing Assistance</li>
      <li>- One-on-One Coaching</li>
    </ul>
  </article>

  <div class="contact" style="left:70px;">
    <span class="contact__label">CONTACT US!</span>
    <span class="contact__item"><svg width="12" height="9" viewBox="0 0 12 9" aria-hidden="true"><rect width="12" height="9" fill="var(--red)"/><path d="M0 0L6 5L12 0" fill="none" stroke="#fff" stroke-width="1"/></svg>info@keystonecommons.org</span>
    <span class="contact__item"><svg width="11" height="11" viewBox="0 0 11 11" aria-hidden="true"><circle cx="5.5" cy="5.5" r="4.7" fill="none" stroke="var(--red)" stroke-width="1.4"/><circle cx="5.5" cy="5.5" r="2" fill="var(--red)"/></svg>keystonecommons.org</span>
  </div>
</section>

</body>
</html>
```